Fabric Softener

We need fabric softener. Bottle picture attached for reference. Color of bottle can be proposed as well. Normally bottle is pink and blue color

Logo is also attached that shall be used.
Updates

Need extra days to review

Low designer entries

Target Market(s)

Niche

Font styles to use
Sans Serif

Requirements
Must have
• Fabric, Brightness, Nature
Nice to have
• Good colors
Should not have
• Adults

```html
<!DOCTYPE html>
<html lang="en">
<head>
<meta charset="utf-8">
<title>Softwave Fabric Softener Bottle</title>
<link rel="stylesheet" href="https://fonts.googleapis.com/css2?family=Oswald:wght@600&family=Open+Sans:ital,wght@0,700;1,800&display=swap">
<style>
  :root {
    --bg: #ffffff;
    --bottle: #9268f2;
    --bottle-light: #a47ff7;
    --bottle-shade: #7f54e6;
    --cap: #f4f4f6;
    --cap-line: #dcdce2;
    --label-light: #fbe6f0;
    --label-mid: #f1bcd6;
    --label-deep: #e690bd;
    --magenta: #e0458f;
    --magenta-dark: #c8287a;
    --brand-purple: #7a2f86;
    --white: #ffffff;
    --tick-red: #d62f45;
    --badge-blue: #2a4a9c;
  }
  html, body {
    margin: 0;
    padding: 0;
    width: 1200px;
    height: 1200px;
    overflow: hidden;
    background: var(--bg);
  }
  .canvas {
    position: relative;
    width: 1200px;
    height: 1200px;
  }
  .bottle-art {
    position: absolute;
    left: 0;
    top: 0;
  }
  .tag-new {
    position: absolute;
    left: 458px;
    top: 506px;
    font: italic 800 36px/1 "Open Sans", sans-serif;
    color: var(--white);
    transform: rotate(-8deg);
  }
  .brand {
    position: absolute;
    left: 392px;
    top: 680px;
    display: flex;
    align-items: center;
    gap: 6px;
  }
  .brand-name {
    font: 700 36px/1 "Open Sans", sans-serif;
    color: var(--brand-purple);
    letter-spacing: -0.5px;
  }
  .brand-dot {
    width: 10px;
    height: 10px;
    border-radius: 50%;
    background: var(--brand-purple);
  }
  .product-name {
    position: absolute;
    left: 391px;
    top: 812px;
    margin: 0;
    font: 600 56px/58px "Oswald", sans-serif;
    color: var(--magenta);
    text-transform: uppercase;
    -webkit-text-stroke: 2px var(--white);
    paint-order: stroke fill;
    text-shadow: 1px 2px 0 var(--magenta-dark);
  }
  .benefits {
    position: absolute;
    left: 472px;
    top: 965px;
    margin: 0;
    padding: 0;
    list-style: none;
    font: italic 800 13px/14px "Open Sans", sans-serif;
    color: var(--white);
  }
  .benefits li {
    display: flex;
    align-items: flex-start;
    gap: 6px;
    margin-bottom: 7px;
  }
  .benefits svg {
    flex: none;
  }
  .bubbles {
    position: absolute;
    left: 640px;
    top: 812px;
    width: 140px;
    height: 200px;
    border-radius: 70px;
    background: radial-gradient(circle at 50% 45%, var(--label-deep), rgba(230,144,189,0) 70%);
  }
  .origin-badge {
    position: absolute;
    left: 658px;
    top: 1008px;
    width: 40px;
    height: 40px;
    border-radius: 50%;
    background: var(--badge-blue);
  }
</style>
</head>
<body>
<main class="canvas">
  <svg class="bottle-art" width="1200" height="1200" viewBox="0 0 1200 1200" aria-hidden="true">
    <defs>
      <linearGradient id="bodyFill" x1="0" y1="0" x2="1" y2="0">
        <stop offset="0" stop-color="var(--bottle-light)"/>
        <stop offset="0.6" stop-color="var(--bottle)"/>
        <stop offset="1" stop-color="var(--bottle-shade)"/>
      </linearGradient>
      <linearGradient id="labelFill" x1="0" y1="0" x2="1" y2="1">
        <stop offset="0" stop-color="var(--label-light)"/>
        <stop offset="0.55" stop-color="var(--label-mid)"/>
        <stop offset="1" stop-color="var(--label-deep)"/>
      </linearGradient>
      <clipPath id="labelClip">
        <path d="M385 1050 L385 700 Q385 540 440 490 Q480 468 512 478 Q545 490 560 530 L620 760 Q640 802 690 805 L790 808 Q815 810 815 835 L815 1045 Q815 1078 785 1080 L415 1080 Q385 1078 385 1050 Z"/>
      </clipPath>
    </defs>

    <!-- cap and collar -->
    <rect class="cap" x="522" y="174" width="156" height="120" rx="10" fill="var(--cap)" stroke="var(--cap-line)" stroke-width="2"/>
    <line x1="560" y1="182" x2="560" y2="290" stroke="var(--cap-line)" stroke-width="2"/>
    <line x1="600" y1="182" x2="600" y2="290" stroke="var(--cap-line)" stroke-width="2"/>
    <line x1="640" y1="182" x2="640" y2="290" stroke="var(--cap-line)" stroke-width="2"/>
    <path class="collar" d="M505 348 L512 300 Q515 286 530 286 L670 286 Q685 286 688 300 L698 348 Z" fill="var(--cap)" stroke="var(--cap-line)" stroke-width="2"/>

    <!-- bottle body -->
    <path class="bottle-body" d="M500 346 L705 346 Q745 370 770 420 Q800 480 815 560 L832 700 Q840 800 835 900 L830 1050 Q828 1100 780 1108 Q600 1120 420 1108 Q385 1104 383 1060 L370 880 Q362 780 372 700 Q390 560 440 460 Q470 390 500 346 Z" fill="url(#bodyFill)"/>
    <ellipse class="handle-hole" cx="678" cy="588" rx="48" ry="112" transform="rotate(-22 678 588)" fill="var(--bg)"/>

    <!-- label -->
    <path class="label-panel" d="M385 1050 L385 700 Q385 540 440 490 Q480 468 512 478 Q545 490 560 530 L620 760 Q640 802 690 805 L790 808 Q815 810 815 835 L815 1045 Q815 1078 785 1080 L415 1080 Q385 1078 385 1050 Z" fill="url(#labelFill)"/>
    <g clip-path="url(#labelClip)">
      <path class="new-band" d="M380 460 L600 460 L600 540 Q490 555 380 600 Z" fill="var(--magenta)"/>
      <path d="M380 600 Q490 555 600 540" stroke="var(--white)" stroke-width="3" fill="none" opacity="0.7"/>
      <path class="swoosh" d="M380 760 Q520 830 670 790" stroke="var(--magenta)" stroke-width="3" fill="none"/>
      <path class="swoosh" d="M650 790 Q620 900 560 1085" stroke="var(--white)" stroke-width="3" fill="none" opacity="0.8"/>
      <path class="base-band" d="M380 985 Q600 925 820 965 L820 1085 L380 1085 Z" fill="var(--magenta)" opacity="0.85"/>
      <path d="M380 985 Q600 925 820 965" stroke="var(--magenta-dark)" stroke-width="3" fill="none"/>
    </g>
  </svg>

  <div class="tag-new">New</div>

  <div class="brand">
    <span class="brand-name">Softwave</span>
    <span class="brand-dot"></span>
  </div>

  <h1 class="product-name">Fabric<br>Softener</h1>

  <div class="bubbles" role="img" aria-label="Soft pink bubbles floating across the label"></div>

  <ul class="benefits">
    <li><svg width="14" height="14" viewBox="0 0 30 30"><circle cx="15" cy="15" r="13" fill="var(--white)"/><path d="M8 15 L13 21 L23 8" stroke="var(--tick-red)" stroke-width="4" fill="none" stroke-linecap="round"/></svg>Eco-Friendly</li>
    <li><svg width="14" height="14" viewBox="0 0 30 30"><circle cx="15" cy="15" r="13" fill="var(--white)"/><path d="M8 15 L13 21 L23 8" stroke="var(--tick-red)" stroke-width="4" fill="none" stroke-linecap="round"/></svg>Easy to Use</li>
    <li><svg width="14" height="14" viewBox="0 0 30 30"><circle cx="15" cy="15" r="13" fill="var(--white)"/><path d="M8 15 L13 21 L23 8" stroke="var(--tick-red)" stroke-width="4" fill="none" stroke-linecap="round"/></svg><span>For everyday<br>Household Needs</span></li>
  </ul>

  <div class="origin-badge" aria-hidden="true"></div>
</main>
</body>
</html>
```